Handmade candle business in melbourne requiring assistance with designing classy labels

My business name is Wick and Willow.
I specialise in making handmade candles, i'm based in Melbourne.
My moto is "Delicately hand poured and infused by me...for you"
wickwillow@mailbox-demo.net
0487 913 072

I need some assistance with designing my labels for my glass candles
I really like earthy colours and nothing too bright, but I want it to look classy and elegant and something that stands out from other homemade candle businesses.
I have attached a sample of a design that appeals to me but open to suggestions.

```html
<!DOCTYPE html>
<html lang="en">
<head>
<meta charset="utf-8">
<title>Wick and Willow – Candle Label</title>
<link rel="stylesheet" href="https://fonts.googleapis.com/css2?family=Gelasio:wght@400&family=Tinos:wght@400&display=swap">
<style>
  :root {
    --page-bg: #ffffff;
    --brand-salmon: #f3967b;
    --body-rose: #c97a80;
    --ink: #111111;
    --label-bg: #ffffff;
    --label-shadow: rgba(0, 0, 0, 0.12);
    --wreath-pink: #f2c3c9;
    --wreath-green: #bfe0c0;
  }
  * { margin: 0; padding: 0; box-sizing: border-box; }
  html, body {
    width: 1200px;
    height: 1000px;
    overflow: hidden;
    background: var(--page-bg);
  }
  .canvas {
    position: relative;
    width: 1200px;
    height: 1000px;
    overflow: hidden;
  }
  .brand-name {
    position: absolute;
    left: 0;
    width: 1200px;
    text-align: center;
    font-family: "Gelasio", Georgia, serif;
    font-weight: 400;
    color: var(--brand-salmon);
    line-height: 1;
    white-space: nowrap;
  }
  .brand-name--header { top: 146px; font-size: 78px; }
  .label {
    position: absolute;
    left: 251px;
    top: 271px;
    width: 698px;
    height: 698px;
    border-radius: 50%;
    background: var(--label-bg);
    box-shadow: 0 0 8px var(--label-shadow);
  }
  .label__wreath {
    position: absolute;
    left: 0;
    top: 0;
    width: 698px;
    height: 698px;
  }
  .label .brand-name--label {
    top: 186px;
    left: 0;
    width: 698px;
    font-size: 58px;
  }
  .label__about {
    position: absolute;
    left: 0;
    width: 698px;
    top: 278px;
    text-align: center;
    font-family: "Gelasio", Georgia, serif;
    font-size: 26px;
    line-height: 38px;
    color: var(--body-rose);
  }
  .label__contact {
    position: absolute;
    left: 0;
    width: 698px;
    text-align: center;
    font-family: "Tinos", "Times New Roman", serif;
    font-size: 27px;
    color: var(--ink);
    line-height: 1;
  }
  .label__email { top: 458px; }
  .label__phone { top: 503px; }
  .label__weight { top: 563px; }
</style>
</head>
<body>
<main class="canvas">
  <h1 class="brand-name brand-name--header">Wick and Willow</h1>

  <section class="label">
    <svg class="label__wreath" viewBox="0 0 698 698" role="img" aria-label="Floral wreath of pink roses and green leaves around the label">
      <defs>
        <linearGradient id="wreathTone" x1="0" y1="0" x2="1" y2="1">
          <stop offset="0" stop-color="var(--wreath-green)"/>
          <stop offset="0.5" stop-color="var(--wreath-pink)"/>
          <stop offset="1" stop-color="var(--wreath-green)"/>
        </linearGradient>
      </defs>
      <circle cx="349" cy="349" r="300" fill="none" stroke="url(#wreathTone)" stroke-width="62" opacity="0.75"/>
    </svg>

    <h2 class="brand-name brand-name--label">Wick and Willow</h2>

    <p class="label__about">
      I specialise in making handmade<br>
      candles, I'm based in Melbourne.<br>
      My moto is "Delicately hand poured<br>
      and infused by me...for you"
    </p>

    <p class="label__contact label__email">wickwillow@mailbox-demo.net</p>
    <p class="label__contact label__phone">0487 913 072</p>
    <p class="label__contact label__weight">250 g</p>
  </section>
</main>
</body>
</html>
```